Art Nouveau Style Round Wine Label

I'd like to design a wine label:
- round
- Using art nouveau type feel similar to attached graphic
- Label should have the text: Morrowfen Vineyard, Pinot Noir, 2023

Target Market(s)

Private buyers - a unique small batch of wine

Industry/Entity Type

Wine

Colors
0054AA
0677BA
7BADD7
CADEEF
E8F1F8
0094D4
00A9DD
6FCCEA
C7EBF8
E9F6FB
00AB8E
00BBA5
67D7C9
C6EFE9
E9F9F6

Requirements
Must have
• Art Nouveau feel similar to the posted picture
Nice to have
• Keys and or Grape bunches incorporated instead of women's faces that are on the example graphic I posted

```html
<!DOCTYPE html>
<html lang="en">
<head>
<meta charset="utf-8">
<title>Morrowfen Vineyard – Pinot Noir 2023</title>
<link rel="stylesheet" href="https://fonts.googleapis.com/css2?family=Cinzel:wght@400;700&family=Yanone+Kaffeesatz:wght@300;400&family=Josefin+Sans:wght@300&family=Pinyon+Script&display=swap">
<style>
  :root {
    --olive-ground: #4a4408;
    --peach: #f7c68a;
    --ring-white: #eceae2;
    --ribbon-green: #9b984c;
    --badge-green: #0f2a17;
    --medallion-light: #b7a26a;
    --medallion-dark: #2e2a10;
  }
  html, body {
    margin: 0;
    padding: 0;
    width: 1120px;
    height: 1200px;
    overflow: hidden;
    background: var(--olive-ground);
  }
  .wine-label {
    display: block;
    width: 1120px;
    height: 1200px;
  }
  .ring-thin { fill: none; stroke: var(--peach); stroke-width: 3; }
  .ring-white { fill: none; stroke: var(--ring-white); stroke-width: 9; }
  .varietal {
    font-family: "Yanone Kaffeesatz", sans-serif;
    font-weight: 300;
    font-size: 78px;
    fill: var(--peach);
  }
  .rule { stroke: var(--peach); stroke-width: 3; }
  .quality-tag {
    font-family: "Cinzel", serif;
    font-weight: 700;
    font-size: 27px;
    fill: var(--peach);
    letter-spacing: 1px;
  }
  .vintage-badge { fill: var(--badge-green); stroke: var(--peach); stroke-width: 3; }
  .vintage-digits {
    font-family: "Josefin Sans", sans-serif;
    font-weight: 300;
    font-size: 44px;
    fill: var(--peach);
  }
  .ribbon-band { fill: var(--ribbon-green); stroke: var(--peach); stroke-width: 5; stroke-linejoin: round; }
  .ribbon-tail { fill: var(--peach); }
  .estate-name {
    font-family: "Cinzel", serif;
    font-weight: 700;
    font-size: 70px;
    fill: var(--peach);
    letter-spacing: 3px;
  }
  .estate-word {
    font-family: "Pinyon Script", cursive;
    font-size: 78px;
    fill: var(--peach);
  }
</style>
</head>
<body>
<svg class="wine-label" viewBox="0 0 1120 1200" xmlns="http://www.w3.org/2000/svg">
  <defs>
    <radialGradient id="medallion-tone" cx="50%" cy="50%" r="50%">
      <stop offset="0%" stop-color="#8a8a4a"/>
      <stop offset="55%" stop-color="var(--medallion-light)"/>
      <stop offset="85%" stop-color="#5a5020"/>
      <stop offset="100%" stop-color="var(--medallion-dark)"/>
    </radialGradient>
    <path id="estate-arc" d="M 270 852 Q 562 798 855 852"/>
  </defs>

  <!-- frame rings -->
  <circle class="ring-thin" cx="561" cy="600" r="408"/>
  <circle class="ring-white" cx="561" cy="600" r="388"/>
  <circle class="ring-thin" cx="561" cy="600" r="370"/>

  <!-- heading -->
  <text class="varietal" x="562" y="345" text-anchor="middle">Pinot Noir</text>
  <line class="rule" x1="307" y1="386" x2="813" y2="386"/>
  <text class="quality-tag" x="385" y="424" text-anchor="middle">Quality</text>
  <text class="quality-tag" x="760" y="424" text-anchor="middle">Wine</text>

  <!-- central medallion artwork area -->
  <circle cx="570" cy="576" r="178" fill="url(#medallion-tone)" stroke="var(--medallion-dark)" stroke-width="4"
          role="img" aria-label="Round Art Nouveau medallion of grape bunches, vine leaves and keys"/>

  <!-- vintage badges -->
  <path class="vintage-badge" d="M 290 595 L 360 595 L 372 607 L 372 682 L 360 694 L 342 694 L 325 706 L 308 694 L 290 694 L 278 682 L 278 607 Z"/>
  <text class="vintage-digits" x="325" y="659" text-anchor="middle">20</text>
  <path class="vintage-badge" d="M 763 595 L 833 595 L 845 607 L 845 682 L 833 694 L 815 694 L 798 706 L 781 694 L 763 694 L 751 682 L 751 607 Z"/>
  <text class="vintage-digits" x="798" y="659" text-anchor="middle">23</text>

  <!-- ribbon banner -->
  <path class="ribbon-tail" d="M 262 820 L 225 862 L 288 868 L 300 905 L 320 872 Z"/>
  <path class="ribbon-tail" d="M 862 820 L 899 862 L 836 868 L 824 905 L 804 872 Z"/>
  <path class="ribbon-band" d="M 255 768 Q 562 712 870 768 L 858 885 Q 562 820 268 885 Z"/>
  <text class="estate-name" text-anchor="middle">
    <textPath href="#estate-arc" startOffset="50%">MORROWFEN</textPath>
  </text>
  <text class="estate-word" x="570" y="930" text-anchor="middle">Vineyard</text>
</svg>
</body>
</html>
```